Re-design UI/UX for Online movie website

We need a stunning design for our online movie website www.vormalite.com

KALDORVUE is an online platform for the presentation of all visual art forms, particularly movies, feature films, short films, documentaries, game shows, reality shows, serials and traditional art forms of different languages for our international audience to indulge in.

We want a design & layout similar to leading online movie streaming websites such as Brimcast , Tavelo Crest , PLUMA BAY

Target Market(s)

Worldwide

Industry/Entity Type

Movie

Number of Pages Required

5+ page

Requirements
Must have
• Look & Feel - These are some of the suggestion. Please feel free to add as per industry standards. Be as creative as possible. The website needs to be really attractive. Movie listing , categories etc., should be easy to navigate
• 1 Text could be justified in all the pages
• 2 Font color may be changed to white color to be more visible.
• 3 Headings to be in Red color instead of Orange color. As Red will match the logo color as well
• 4 Heading to be consistent everywhere. Example in About us page " About us" font is capital, white in color and larger than the other 2 headings on the same page.
• 5 Chatterly, quibbr and Snapgrove links to be added
• 6 Menu options could be in white or red color to be more visible. Current grey color is looking dull.
• 8 One more menu tab to be included on the top named "Movies" or "Browse movies" . Under Browse Movies, add multilevel menu "New Releases" "Short Films" "Kaldorvue Originals" "Library" "All Movies" . Later categories like Comedy, Thriller etc, can be added
• 9 Add “Watch movie” or “Watch Trailer” on the banner Images
• 10 Give “back to home link” on all subpages
• 11 The Grid format showing movie thumbnails can be made better with border (red or white)

```html
<!DOCTYPE html>
<html lang="en">
<head>
<meta charset="utf-8">
<title>KALDORVUE — Online Movies</title>
<link href="https://fonts.googleapis.com/css2?family=Overpass:wght@400;600;700;800;900&display=swap" rel="stylesheet">
<style>
:root{
  --red:#e8192c;
  --red-dark:#c81222;
  --black:#050505;
  --ink:#2a2a33;
  --grey:#6e6e73;
  --link:#2a5bd7;
  --select-blue:#4a6fd8;
  --slate:#2e3138;
  --white:#ffffff;
}
*{box-sizing:border-box;margin:0;padding:0}
html,body{width:1200px;height:1000px;overflow:hidden;background:var(--white);font-family:"Overpass",Arial,sans-serif}
.page{position:relative;width:1200px;height:1000px;overflow:hidden}

/* Header */
.site-header{position:absolute;left:0;top:0;width:1200px;height:62px;background:var(--black);color:var(--white)}
.brand{position:absolute;left:42px;top:13px;display:flex;flex-direction:column}
.brand-name{font-size:22px;font-weight:700;color:var(--red);letter-spacing:1px;line-height:22px;display:flex;align-items:center;gap:6px}
.brand-mark{width:8px;height:8px;background:var(--white)}
.brand-tag{font-size:8px;color:var(--white);margin-left:14px;margin-top:2px}
.main-nav{position:absolute;left:0;top:0;height:62px;width:922px}
.main-nav a{position:absolute;top:0;height:62px;display:flex;align-items:center;color:var(--white);text-decoration:none;font-size:10.5px;font-weight:600;white-space:nowrap}
.main-nav a .caret{font-size:8px;margin-left:3px;opacity:.8}
.main-nav a.active::after{content:"";position:absolute;left:8px;right:-10px;bottom:0;height:2px;background:var(--red)}
.divider{position:absolute;top:0;width:1px;height:62px;background:#2b2b2b}
.call{position:absolute;left:948px;top:19px;display:flex;gap:10px}
.call-label{font-size:7px;font-weight:600;letter-spacing:.3px}
.call-number{font-size:13px;font-weight:700;color:var(--red)}
.follow{position:absolute;left:1088px;top:18px}
.follow-label{font-size:7px;font-weight:600;letter-spacing:.3px}
.social{display:flex;gap:7px;margin-top:7px}
.social span{width:7px;height:7px;border-radius:50%;background:var(--white)}

/* Hero */
.hero{position:absolute;left:0;top:62px;width:1200px;height:440px}
.hero-photo{position:absolute;inset:0;background:
  radial-gradient(ellipse at 30% 50%,rgba(120,130,145,.55),transparent 60%),
  linear-gradient(180deg,#3a3e47 0%,#5a5f69 40%,#8c9098 70%,#ffffff 100%)}
.hero-title{position:absolute;left:0;width:1225px;top:98px;text-align:center;color:var(--white);font-size:58px;font-weight:900;letter-spacing:1px}
.hero-sub{position:absolute;left:0;width:1225px;top:163px;text-align:center;color:var(--white);font-size:14px;letter-spacing:1.5px}
.btn-watch{position:absolute;left:502px;top:192px;width:222px;height:52px;background:var(--red);border-radius:3px;color:var(--white);font-size:22px;font-weight:800;letter-spacing:1.5px;display:flex;align-items:center;padding-left:11px}
.btn-watch svg{position:absolute;right:12px;top:16px}

/* Search panel */
.search-panel{position:absolute;left:243px;top:338px;width:713px;height:132px;background:var(--red)}
.tabs{display:flex;height:37px;border-bottom:1px solid var(--red-dark)}
.tab{font-size:11px;font-weight:600;color:var(--white);display:flex;align-items:center;padding-left:19px}
.tab-count{width:157px;background:var(--red-dark)}
.select{position:absolute;width:168px;height:27px;background:var(--white);font-size:8.5px;color:var(--ink);display:flex;align-items:center;padding-left:12px}
.select svg{position:absolute;right:11px;top:10px}
.btn-search{position:absolute;left:526px;top:85px;width:168px;height:27px;background:var(--slate);color:var(--white);font-size:10px;font-weight:600;letter-spacing:1px;display:flex;align-items:center;justify-content:center;gap:6px}
.options{position:absolute;left:19px;top:83px;width:168px;background:var(--white);box-shadow:0 2px 6px rgba(0,0,0,.2);padding:3px 0 4px}
.options div{font-size:8.5px;color:var(--ink);height:19px;display:flex;align-items:center;padding-left:12px}
.options .selected{background:var(--select-blue);color:var(--white)}

/* Welcome */
.welcome-title{position:absolute;left:243px;top:560px;font-size:29px;font-weight:800;line-height:36px;color:var(--ink)}
.welcome-text{position:absolute;left:488px;top:572px;width:468px;font-size:11px;line-height:17.5px;color:var(--grey);text-align:justify;hyphens:auto;-webkit-hyphens:auto}

/* Cards */
.card{position:absolute;top:680px;width:165px}
.card-image{width:165px;height:112px}
.card-title{margin-top:18px;font-size:15px;color:var(--ink);font-weight:400}
.card-text{margin-top:9px;font-size:9px;line-height:15px;color:var(--grey);hyphens:auto;-webkit-hyphens:auto}
.card-link{display:inline-block;margin-top:14px;font-size:9px;color:var(--link);text-decoration:none;white-space:nowrap}
.card-link .underline{text-decoration:underline}
.footer-band{position:absolute;left:0;top:972px;width:1200px;height:28px;background:linear-gradient(90deg,#1b1b1d,#2c2c2f,#1b1b1d)}
</style>
</head>
<body>
<div class="page">
  <header class="site-header">
    <div class="brand">
      <div class="brand-name"><span class="brand-mark"></span>KALDORVUE</div>
      <div class="brand-tag">stories for every screen</div>
    </div>
    <nav class="main-nav">
      <a href="#" aria-label="Home" style="left:346px">
        <svg width="20" height="17" viewBox="0 0 20 17"><path d="M10 1 L1 9 H4 V16 H8 V11 H12 V16 H16 V9 H19 Z" fill="#fff"/></svg>
      </a>
      <a href="#" style="left:380px">About Us<span class="caret">⌄</span></a>
      <a href="#" class="active" style="left:450px">Browse Movies<span class="caret">⌄</span></a>
      <a href="#" style="left:550px">New Releases<span class="caret">⌄</span></a>
      <a href="#" style="left:638px">Short Films<span class="caret">⌄</span></a>
      <a href="#" style="left:713px">Originals<span class="caret">⌄</span></a>
      <a href="#" style="left:780px">Library<span class="caret">⌄</span></a>
      <a href="#" style="left:834px">All Movies<span class="caret">⌄</span></a>
    </nav>
    <span class="divider" style="left:922px"></span>
    <span class="divider" style="left:1080px"></span>
    <div class="call">
      <svg width="14" height="14" viewBox="0 0 14 14" style="margin-top:7px"><path d="M3 1 L5 4 L4 5.5 C5 7.5 6.5 9 8.5 10 L10 9 L13 11 L12 13 C6 13 1 8 1 2 Z" fill="none" stroke="#e8192c" stroke-width="1.3"/></svg>
      <div>
        <div class="call-label">CALL US TODAY</div>
        <div class="call-number">800-555-01-27</div>
      </div>
    </div>
    <div class="follow">
      <div class="follow-label">FOLLOW US</div>
      <div class="social"><span></span><span></span><span></span><span></span><span></span><span></span></div>
    </div>
  </header>

  <section class="hero">
    <div class="hero-photo" role="img" aria-label="Blurred tablet showing a grid of movie thumbnails beside a laptop keyboard"></div>
    <h1 class="hero-title">See what’s next.</h1>
    <p class="hero-sub">WATCH ANYWHERE.CANCEL ANYTIME.</p>
    <div class="btn-watch">WATCH MOVIE
      <svg width="14" height="22" viewBox="0 0 14 22"><path d="M2 2 L11 11 L2 20" fill="none" stroke="#fff" stroke-width="3"/></svg>
    </div>
  </section>

  <section class="search-panel">
    <div class="tabs">
      <div class="tab tab-count">11,6579 MOVIES</div>
      <div class="tab">Advanced Search</div>
    </div>
    <div class="select" style="left:19px;top:56px">New Movie Title<svg width="12" height="7" viewBox="0 0 12 7"><path d="M1 1 L6 6 L11 1" fill="none" stroke="#888"/></svg></div>
    <div class="select" style="left:188px;top:56px">CATEGORY 1<svg width="12" height="7" viewBox="0 0 12 7"><path d="M1 1 L6 6 L11 1" fill="none" stroke="#888"/></svg></div>
    <div class="select" style="left:357px;top:56px">CATEGORY 2<svg width="12" height="7" viewBox="0 0 12 7"><path d="M1 1 L6 6 L11 1" fill="none" stroke="#888"/></svg></div>
    <div class="select" style="left:526px;top:56px">CATEGORY 3<svg width="12" height="7" viewBox="0 0 12 7"><path d="M1 1 L6 6 L11 1" fill="none" stroke="#888"/></svg></div>
    <div class="select" style="left:188px;top:85px">CATEGORY &nbsp;4<svg width="12" height="7" viewBox="0 0 12 7"><path d="M1 1 L6 6 L11 1" fill="none" stroke="#888"/></svg></div>
    <div class="select" style="left:357px;top:85px">CATEGORY 5<svg width="12" height="7" viewBox="0 0 12 7"><path d="M1 1 L6 6 L11 1" fill="none" stroke="#888"/></svg></div>
    <div class="btn-search">
      <svg width="10" height="10" viewBox="0 0 10 10"><circle cx="4" cy="4" r="3" fill="none" stroke="#fff" stroke-width="1.2"/><path d="M6.2 6.2 L9 9" stroke="#fff" stroke-width="1.2"/></svg>SEARCH
    </div>
    <div class="options">
      <div>New Movie Title</div>
      <div class="selected">New Movie Title</div>
      <div>Old Movie Title</div>
    </div>
  </section>

  <h2 class="welcome-title">Welcome to<br>Kaldorvue</h2>
  <p class="welcome-text">Aenean auctor wisi et urna. Aliquam erat volutpat. Duis ac turpis. Integer rutrum ante eu lacus. Vestibulum libero nisl, porta vel, scelerisque eget, malesuada at, neque. Vivamus eget nibh. Etiam cursus leo vel metus. Nulla facilisi. Aenean nec eros.</p>

  <article class="card" style="left:243px">
    <div class="card-image" role="img" aria-label="Action movie poster with a green and yellow title" style="background:linear-gradient(160deg,#6b8a5a,#2e3a2c 60%,#c9b24a)"></div>
    <h3 class="card-title">New Releases</h3>
    <p class="card-text">Mauris fermentum dictum magna. Sed laoreet aliquam leo. Ut tellus dolor, dapibus eget, elementum vel.</p>
    <a class="card-link" href="#">View Inventory &nbsp;»</a>
  </article>
  <article class="card" style="left:426px">
    <div class="card-image" role="img" aria-label="Drama movie poster in grey tones with a white title" style="background:linear-gradient(160deg,#a9a6a4,#4a4646 60%,#2a2a2a)"></div>
    <h3 class="card-title">Research &amp; Reviews</h3>
    <p class="card-text">Aenean auctor wisi et urna. Aliquam erat volutpat. Duis ac turpis. Integer rutrum ante eu lacus.Vestibulum libero nisl.</p>
    <a class="card-link" href="#"><span class="underline">See Research &amp; Reviews</span> &nbsp;»</a>
  </article>
  <article class="card" style="left:609px">
    <div class="card-image" role="img" aria-label="Action movie poster in warm yellow and green with a red title" style="background:linear-gradient(160deg,#d9c77a,#7c8a3e 55%,#3c3a20)"></div>
    <h3 class="card-title">MOST POPULAR</h3>
    <p class="card-text">Mauris fermentum dictum magna. Sed laoreet aliquam leo. Ut tellus dolor, dapibus eget, elementum vel.</p>
    <a class="card-link" href="#">Schedule Now &nbsp;»</a>
  </article>
  <article class="card" style="left:792px">
    <div class="card-image" role="img" aria-label="Movie poster in teal and grey with a red title" style="background:linear-gradient(160deg,#8fa7a3,#4e6663 55%,#8a2a2a)"></div>
    <h3 class="card-title">DOCUMENTARIES</h3>
    <p class="card-text">Mauris fermentum dictum magna. Sed laoreet aliquam leo. Ut tellus dolor, dapibus eget, elementum vel.</p>
    <a class="card-link" href="#">Read More &nbsp;»</a>
  </article>

  <div class="footer-band" role="img" aria-label="Dark footer photo strip"></div>
</div>
</body>
</html>
```